Solar accessories banner to produce more green energy

Hello,
we need a banner for a solar accessories page.
https://plovinta.de/index.php/zubehoer/
as we are commissioning the first banner for the entire homepage here, we are open to all directions. The current existing banner is just a random image of the installed theme and should not be a reference.
The banner should be created in a dark style. Our core colors are black / yellow / white.
The banner should have a clear reference to the accessories shown below and consider other accessories such as mounting systems of solar panels, cables, adapters, etc.
I would be happy to answer any queries.
Regards
Malte
-------------------------------------------------- ----------------------------------------------
Hello,
https://plovinta.de/index. php / accessories /
Since we are commissioning the first banner for the entire homepage, we are open to all directions. The currently existing banner is only a random image of the installed theme and is not intended to be a reference.
The banner should be created in a dark stem. Our core colors are black / yellow / white.
The banner should have a clear reference to the accessories shown below and take into account other accessories such as mounting systems for solar panels, cables, adapters, etc.
I am happy to answer any questions.
greetings
Malte

```html
<!DOCTYPE html>
<html lang="de">
<head>
<meta charset="utf-8">
<title>Plovinta – Zubehör Banner</title>
<link rel="stylesheet" href="https://fonts.googleapis.com/css2?family=Inter:ital,wght@0,300;0,400;0,600;1,400&display=swap">
<style>
:root{
  --bg:#2a2b29;
  --card:#2c2d2b;
  --nav:#000000;
  --yellow:#ffc400;
  --orange:#ffa41e;
  --white:#ffffff;
  --muted:#a9aaa6;
  --line:#bdbdbd;
  --frame:#d9d9d9;
}
*{margin:0;padding:0;box-sizing:border-box}
html,body{width:1200px;height:605px;overflow:hidden}
body{
  background:radial-gradient(ellipse 60% 40% at 50% 0%,#4a4b48 0%,transparent 70%),
             radial-gradient(ellipse 60% 30% at 50% 100%,#4a4b48 0%,transparent 70%),var(--bg);
  font-family:'Inter',sans-serif;position:relative;
}
.banner{
  position:absolute;left:41px;top:47px;width:1118px;height:511px;
  border:1px solid var(--line);border-radius:60px;overflow:hidden;
  background:radial-gradient(ellipse 50% 60% at 30% 55%,#363735 0%,var(--card) 70%);
}
.nav{
  height:40px;background:var(--nav);display:flex;justify-content:center;align-items:center;gap:18px;
  padding-left:30px;
}
.nav a{
  color:#b5b5b5;font-size:6.6px;letter-spacing:1.1px;text-decoration:none;font-weight:400;position:relative;
  line-height:40px;
}
.nav a.active,.nav a.shop{color:var(--white);font-weight:600}
.nav a.active::before{
  content:"";position:absolute;left:-9px;right:-9px;top:0;height:1px;background:#d9c48a;
}
.arrow{position:absolute;top:204px}
.arrow-left{left:136px}
.arrow-right{left:955px}
.splash-area{
  position:absolute;left:96px;top:126px;width:384px;height:262px;
  background:linear-gradient(200deg,rgba(255,196,0,.15) 0%,#ffb81a 55%,var(--orange) 100%);
}
.product-photo{
  position:absolute;left:206px;top:138px;width:256px;height:222px;
  background:linear-gradient(160deg,#3c3d3b 0%,#1e1f1e 60%,#151615 100%);
}
.product-frame{position:absolute;left:198px;top:120px;width:281px;height:277px}
.pager{position:absolute;left:721px;top:91px;display:flex;gap:9px;align-items:center}
.pager span{width:4px;height:4px;border-radius:50%;background:#a88a1e}
.pager span.on{width:6px;height:6px;background:var(--yellow)}
.title{
  position:absolute;left:577px;top:117px;color:var(--white);font-weight:300;font-size:23px;letter-spacing:.2px;
}
.rule{position:absolute;left:690px;top:165px;width:111px;height:1px;background:var(--white)}
.copy{
  position:absolute;left:577px;top:192px;color:var(--muted);white-space:nowrap;
  font-size:15px;font-weight:300;line-height:27px;letter-spacing:.15px;
}
.offer{position:absolute;left:675px;top:320px;width:135px;height:45px}
.offer-text{
  position:absolute;inset:0;display:flex;align-items:center;justify-content:center;
  color:var(--white);font-style:italic;font-size:22px;letter-spacing:.5px;
}
.buy{
  position:absolute;left:687px;top:401px;width:111px;height:27px;border-radius:14px;
  background:var(--yellow);color:#222;font-style:italic;font-size:11px;
  display:flex;align-items:center;justify-content:center;
  box-shadow:0 3px 8px rgba(0,0,0,.4);
}
</style>
</head>
<body>
<section class="banner">
  <nav class="nav">
    <a href="#">PLOVINTA</a>
    <a href="#">MANAGEMENT</a>
    <a href="#">WECHSELRICHTER</a>
    <a href="#">BATTERIESPEICHER</a>
    <a href="#">SOLARMODULE</a>
    <a href="#">AUTOLADESTATIONEN</a>
    <a href="#">HEIZUNG/WARMWASSER</a>
    <a href="#" class="active">ZUBEHÖR</a>
    <a href="#" class="shop">SHOP</a>
  </nav>

  <div class="splash-area" role="img" aria-label="Gelb-oranger Pinselstrich als Hintergrund"></div>
  <div class="product-photo" role="img" aria-label="Produktfoto: schwarze Solarstecker und Y-Adapter"></div>
  <svg class="product-frame" viewBox="0 0 281 277" fill="none">
    <path d="M121 0.5H0.5V276.5H121M160 276.5H280.5V0.5H160" stroke="var(--frame)" stroke-width="0.8"/>
    <circle cx="140.5" cy="0.5" r="2" fill="var(--yellow)"/>
    <circle cx="140.5" cy="276.5" r="2" fill="var(--yellow)"/>
  </svg>

  <svg class="arrow arrow-left" width="12" height="26" viewBox="0 0 12 26"><path d="M10 1L2 13L10 25" stroke="#d0d0d0" stroke-width="1.6" fill="none"/></svg>
  <svg class="arrow arrow-right" width="12" height="26" viewBox="0 0 12 26"><path d="M2 1L10 13L2 25" stroke="#d0d0d0" stroke-width="1.6" fill="none"/></svg>

  <div class="pager"><span class="on"></span><span></span><span></span><span></span><span></span></div>
  <h1 class="title">Montage und Anschluss Zubehör</h1>
  <div class="rule"></div>
  <p class="copy">Unser Zubehörsortiment ist auf die angebotenen<br>Produkte perfekt abgestimmt. So finden Sie zu<br>allen Bereichen passende Stecker, Kabel, Adapter,<br>Halterungen, uvm.</p>

  <div class="offer">
    <svg width="135" height="45" viewBox="0 0 135 45" fill="none" style="position:absolute;inset:0">
      <path d="M58 44H1V1H134V44H77" stroke="#cfcfcf" stroke-width="1.5"/>
      <circle cx="67.5" cy="44" r="2" fill="#a88a1e"/>
    </svg>
    <div class="offer-text">40% OFF</div>
  </div>
  <a class="buy">BUY NOW</a>
</section>
</body>
</html>
```